Restaurant service company needs a website!

I am looking for a skilled web designer/developer to create a professional, responsive, and easy-to-navigate website for my company, which specializes in servicing restaurant cooking equipment. The site should communicate trust, reliability, and technical expertise to our target audience, restaurant owners, managers, and commercial kitchen operators. I have included the company logos, if any other format for them is needed please let me know.

Target Market(s)

restaurant owners, managers, and commercial kitchen operators

Industry/Entity Type

Commercial Kitchen Equipment Service

Coding

Coded - Design and coding required

Number of Pages Required

1 page

Font styles to use
Serif
Sans Serif

Requirements
Must have
• Contact and service request forms, Click-to-call functionality for mobile, Clean, modern layout with strong visuals, Easy navigation, mobile-friendly
Nice to have
• Testimonials or Reviews, If possible a click-to-text functionality for mobile.
Should not have
• Any mention of Refrigeration or HVAC, "Free Quotes"

```html
<!DOCTYPE html>
<html lang="en">
<head>
<meta charset="utf-8">
<title>Junction Kitchen Service</title>
<link href="https://fonts.googleapis.com/css2?family=Schibsted+Grotesk:wght@500;600;700&family=Inter:wght@400;500;600&display=swap" rel="stylesheet">
<style>
:root{
  --teal:#0f6b6b;
  --teal-soft:#e4f0ee;
  --ink:#16181a;
  --muted:#6b6f6c;
  --line:#e6e5df;
  --page:#fbfbf8;
  --band:#f4f3ec;
  --card:#ffffff;
  --footer:#17190f;
  --gold:#f2b71d;
  --canvas:#ffffff;
}
*{box-sizing:border-box;margin:0;padding:0}
html,body{width:1200px;height:1200px;overflow:hidden;background:var(--canvas)}
body{font-family:"Inter",sans-serif;color:var(--ink)}
.site{position:absolute;left:478.6px;top:0;width:1440px;height:7115px;transform:scale(0.16866);transform-origin:0 0;background:var(--page)}
h1,h2,h3,.brand-name,.stat-value{font-family:"Schibsted Grotesk",sans-serif}
.wrap{width:1216px;margin:0 auto;position:relative}
section{position:relative;overflow:hidden}
.section-head{text-align:center}
.section-head h2{font-size:36px;font-weight:600;letter-spacing:-.3px}
.section-head p{font-size:19px;color:var(--muted);line-height:1.5;width:760px;margin:18px auto 0}
.icon-dot{width:56px;height:56px;border-radius:50%;background:var(--teal-soft);display:flex;align-items:center;justify-content:center}
.icon-dot svg{width:24px;height:24px;stroke:var(--teal);fill:none;stroke-width:1.8;stroke-linecap:round;stroke-linejoin:round}
.card{background:var(--card);border:1px solid var(--line);border-radius:10px;box-shadow:0 2px 8px rgba(0,0,0,.04)}

/* nav */
.nav{height:81px;background:#fff;border-bottom:1px solid var(--line)}
.nav .wrap{height:81px;display:flex;align-items:center;justify-content:space-between}
.brand{display:flex;align-items:center;gap:10px}
.brand-mark{width:24px;height:24px;border:3px solid var(--teal);border-radius:4px}
.brand-name{font-size:16px;font-weight:600;color:var(--teal)}
.nav-links{display:flex;align-items:center;gap:32px;font-size:16px;font-weight:500}
.btn{display:inline-flex;align-items:center;gap:10px;background:var(--teal);color:#fff;font-weight:600;border-radius:6px}
.nav .btn{font-size:14px;padding:10px 16px}

/* hero */
.hero{height:751px;color:#fff;text-align:center}
.hero-photo{position:absolute;inset:0;background:linear-gradient(180deg,#3a3c3d 0%,#55585a 45%,#2c3346 78%,#1d2230 100%)}
.hero-shade{position:absolute;inset:0;background:rgba(0,0,0,.35)}
.hero-inner{position:relative;padding-top:124px}
.hero h1{font-size:72px;line-height:1;font-weight:600;letter-spacing:-.5px}
.hero p{font-size:23px;line-height:1.4;width:770px;margin:40px auto 0;opacity:.92}
.hero-actions{display:flex;justify-content:center;gap:28px;margin-top:40px}
.hero-actions .btn{font-size:16px;padding:14px 22px}
.btn-ghost{display:inline-flex;align-items:center;gap:10px;font-size:16px;padding:14px 22px;border-radius:6px;background:rgba(255,255,255,.1)}

/* core services */
.core{height:1046px}
.core .section-head{padding-top:94px}
.core-grid{display:grid;grid-template-columns:repeat(4,1fr);gap:32px;margin-top:70px}
.core-card{height:330px;padding:28px 30px;text-align:center;display:flex;flex-direction:column;align-items:center}
.core-card.short{height:310px}
.core-card h3{font-size:19px;font-weight:600;margin-top:26px;line-height:1.4;white-space:nowrap}
.core-card p{font-size:14px;color:var(--muted);line-height:1.7;margin-top:18px}

/* equipment */
.equip{height:958px;background:var(--band)}
.equip .section-head{padding-top:100px}
.equip-grid{display:grid;grid-template-columns:repeat(3,1fr);gap:32px 33px;margin-top:68px}
.equip-card{height:276px;padding:26px 26px}
.equip-top{display:flex;align-items:center;gap:16px}
.equip-top .icon-dot{width:44px;height:44px;border-radius:8px}
.equip-top .icon-dot svg{width:20px;height:20px}
.equip-top h3{font-size:19px;font-weight:600}
.equip-card p{font-size:14px;color:var(--muted);line-height:1.7;margin-top:20px}
.tags{display:flex;flex-wrap:wrap;gap:10px 10px;margin-top:18px}
.tag{font-size:11px;font-weight:600;background:#eeeee9;border-radius:4px;padding:6px 8px}

/* why */
.why{height:1131px}
.why .section-head{padding-top:96px}
.stats{display:grid;grid-template-columns:repeat(4,1fr);margin-top:64px;text-align:center}
.stat-value{font-size:50px;font-weight:600;color:var(--teal)}
.stat-label{font-size:14px;color:var(--muted);margin-top:8px}
.why-grid{display:grid;grid-template-columns:repeat(3,1fr);gap:33px;margin-top:46px}
.why-card{height:284px;padding:28px 30px;text-align:center;display:flex;flex-direction:column;align-items:center}
.why-card.tall{height:306px}
.pill{font-size:10px;font-weight:600;background:#efefea;border-radius:20px;padding:5px 10px;margin-top:18px}
.why-card h3{font-size:20px;font-weight:600;margin-top:22px}
.why-card p{font-size:14px;color:var(--muted);line-height:1.7;margin-top:20px;width:330px}

/* trusted */
.trusted{height:626px;background:var(--band)}
.trusted .wrap{display:flex;justify-content:space-between;padding-top:112px}
.trusted-copy{width:570px}
.trusted-copy h2{font-size:36px;font-weight:600;line-height:1.1}
.trusted-copy>p{font-size:16px;color:var(--muted);line-height:1.75;margin-top:24px}
.checks{display:grid;grid-template-columns:1fr 1fr;gap:24px 30px;margin-top:34px}
.check{display:flex;gap:12px;font-size:14px;font-weight:500;line-height:1.5;align-items:center}
.check svg{flex:none;width:20px;height:20px;stroke:var(--teal);fill:none;stroke-width:2}
.trusted-visual{position:relative;width:575px;margin-top:12px}
.trusted-frame{background:#fff;padding:8px;border-radius:10px;box-shadow:0 6px 20px rgba(0,0,0,.08)}
.trusted-photo{height:390px;border-radius:6px;background:linear-gradient(135deg,#5e6264 0%,#3f4a57 40%,#2f5f9a 70%,#4b4f53 100%)}
.badge-light{position:absolute;right:-30px;top:-48px;background:#fff;border-radius:8px;padding:16px 24px;box-shadow:0 6px 18px rgba(0,0,0,.1);text-align:center}
.badge-light strong{display:block;font-family:"Schibsted Grotesk",sans-serif;font-size:30px;color:var(--teal);font-weight:600}
.badge-light span{font-size:11px;color:var(--muted)}
.badge-teal{position:absolute;left:-34px;bottom:-46px;background:var(--teal);color:#fff;border-radius:8px;padding:18px 26px 20px;width:178px}
.badge-teal strong{display:block;font-family:"Schibsted Grotesk",sans-serif;font-size:30px;font-weight:600}
.badge-teal span{font-size:11px;opacity:.9}

/* testimonials */
.reviews{height:618px}
.reviews .section-head{padding-top:100px}
.review-grid{display:grid;grid-template-columns:repeat(3,1fr);gap:33px;margin-top:66px}
.review{height:250px;padding:24px 26px}
.stars{color:var(--gold);font-size:20px;letter-spacing:3px}
.review h3{font-size:15px;font-weight:600;margin-top:18px}
.review .role{font-size:11px;color:var(--muted);margin-top:6px}
.review blockquote{font-size:14px;font-style:italic;color:var(--muted);line-height:1.6;margin-top:26px}

/* contact */
.contact{height:1466px;background:var(--band)}
.contact .section-head{padding-top:106px}
.contact-grid{display:grid;grid-template-columns:repeat(4,1fr);gap:28px;margin-top:64px}
.contact-card{height:248px;padding:44px 20px;text-align:center;display:flex;flex-direction:column;align-items:center}
.contact-card .icon-dot{width:48px;height:48px}
.contact-card h3{font-size:15px;font-weight:600;margin-top:20px}
.contact-card .val{font-size:14px;font-weight:600;margin-top:12px}
.contact-card .val.big{font-size:26px;color:var(--teal)}
.contact-card .note{font-size:11px;color:var(--muted);margin-top:10px}
.form-card{width:891px;margin:66px auto 0;height:774px;padding:30px 32px}
.form-title{display:flex;justify-content:center;align-items:center;gap:12px}
.form-title svg{width:24px;height:24px;stroke:var(--teal);fill:none;stroke-width:2}
.form-title h3{font-size:24px;font-weight:600}
.form-sub{text-align:center;font-size:16px;color:var(--muted);margin-top:12px}
.form-cols{display:grid;grid-template-columns:1fr 1fr;gap:36px;margin-top:100px}
.form-cols h4{font-family:"Schibsted Grotesk",sans-serif;font-size:16px;font-weight:600;padding-bottom:14px;border-bottom:1px solid var(--line)}
.field{margin-top:30px}
.field label{font-size:12px;font-weight:600;display:block}
.input{height:38px;border:1px solid var(--line);border-radius:5px;margin-top:10px;background:#fff;font-size:11px;color:var(--muted);padding:12px 12px}
.input.select{width:168px}
.input.area{height:74px;line-height:1.6;padding-top:10px}
.submit{display:flex;justify-content:center;width:100%;margin-top:60px;padding:18px;font-size:17px}
.form-note{text-align:center;font-size:11px;color:var(--muted);margin-top:22px}

/* footer */
.footer{height:438px;background:var(--footer);color:#e9e9e3}
.footer .wrap{padding-top:64px}
.footer-top{display:flex}
.footer-about{width:620px}
.footer .brand-name{color:#e9e9e3}
.footer .brand-mark{border-color:#e9e9e3}
.footer-about p{font-size:14px;line-height:1.7;margin-top:44px;width:430px}
.footer-about .line{font-size:14px;margin-top:14px}
.footer-about .line b{font-weight:600}
.footer-col{width:310px}
.footer-col h4{font-size:14px;font-weight:600}
.footer-col li{list-style:none;font-size:14px;margin-top:14px;opacity:.85}
.footer-bottom{display:flex;justify-content:space-between;border-top:1px solid #33352b;margin-top:44px;padding-top:26px;font-size:12px;opacity:.75}
.footer-bottom nav{display:flex;gap:24px}
</style>
</head>
<body>
<div class="site">

<header class="nav">
  <div class="wrap">
    <div class="brand"><span class="brand-mark"></span><span class="brand-name">Junction</span></div>
    <nav class="nav-links"><span>Services</span><span>About</span><span>Reviews</span><span>Contact</span><span class="btn">Request Service</span></nav>
  </div>
</header>

<section class="hero">
  <div class="hero-photo" role="img" aria-label="Commercial kitchen range with stainless pots and blue burner knobs"></div>
  <div class="hero-shade"></div>
  <div class="hero-inner wrap">
    <h1>Expert Service for<br>Your Commercial<br>Kitchen Equipment</h1>
    <p>Professional repair and maintenance services for restaurants, hotels, and commercial kitchens. Keeping your cooking equipment running at peak performance.</p>
    <div class="hero-actions">
      <span class="btn">Request Service Now <svg width="16" height="16" viewBox="0 0 16 16" fill="none" stroke="#fff" stroke-width="2"><path d="M3 8h10M9 4l4 4-4 4"/></svg></span>
      <span class="btn-ghost"><svg width="16" height="16" viewBox="0 0 24 24" fill="none" stroke="#fff" stroke-width="2"><path d="M5 3h4l2 5-3 2a11 11 0 0 0 6 6l2-3 5 2v4a2 2 0 0 1-2 2A17 17 0 0 1 3 5a2 2 0 0 1 2-2z"/></svg>Call (555) 014-2368</span>
    </div>
  </div>
</section>

<section class="core">
  <div class="wrap">
    <div class="section-head">
      <h2>Our Core Services</h2>
      <p>Comprehensive solutions to keep your commercial kitchen equipment operating at peak performance</p>
    </div>
    <div class="core-grid">
      <div class="card core-card"><div class="icon-dot"><svg viewBox="0 0 24 24"><path d="M14 6a4 4 0 0 0 5 5l-9 9a2 2 0 0 1-3-3l9-9"/></svg></div><h3>Equipment Repair</h3><p>Expert repair services for all types of commercial cooking equipment including ovens, grills, fryers, and ranges.</p></div>
      <div class="card core-card"><div class="icon-dot"><svg viewBox="0 0 24 24"><circle cx="12" cy="12" r="9"/><path d="M12 7v5l3 2"/></svg></div><h3>Preventive<br>Maintenance</h3><p>Scheduled maintenance programs to keep your equipment running efficiently and prevent costly breakdowns.</p></div>
      <div class="card core-card"><div class="icon-dot"><svg viewBox="0 0 24 24"><path d="M12 3l8 3v6c0 5-4 8-8 9-4-1-8-4-8-9V6z"/></svg></div><h3>Emergency Service</h3><p>24/7 emergency repair services to minimize downtime and keep your kitchen operational.</p></div>
      <div class="card core-card"><div class="icon-dot"><svg viewBox="0 0 24 24"><circle cx="9" cy="8" r="3"/><path d="M3 20a6 6 0 0 1 12 0M16 5a3 3 0 0 1 0 6M21 20a6 6 0 0 0-4-6"/></svg></div><h3>Staff Training</h3><p>Comprehensive training programs for your kitchen staff on proper equipment operation and basic maintenance.</p></div>
      <div class="card core-card short"><div class="icon-dot"><svg viewBox="0 0 24 24"><path d="M12 3c3 4 6 6 6 11a6 6 0 0 1-12 0c0-3 2-5 3-6 0 2 1 3 2 3 0-3 0-5 1-8z"/></svg></div><h3>Gas Line Services</h3><p>Professional gas line installation, repair, and safety inspections for all commercial cooking equipment.</p></div>
      <div class="card core-card short"><div class="icon-dot"><svg viewBox="0 0 24 24"><path d="M4 16a8 8 0 0 1 16 0M12 16l4-5"/></svg></div><h3>Performance<br>Optimization</h3><p>Equipment calibration and optimization services to ensure maximum efficiency and energy savings.</p></div>
      <div class="card core-card short"><div class="icon-dot"><svg viewBox="0 0 24 24"><circle cx="12" cy="12" r="9"/><path d="M8 12l3 3 5-6"/></svg></div><h3>Safety Inspections</h3><p>Comprehensive safety inspections and compliance checks to meet health department requirements.</p></div>
      <div class="card core-card short"><div class="icon-dot"><svg viewBox="0 0 24 24"><path d="M13 3L5 14h6l-1 7 8-11h-6z"/></svg></div><h3>Electrical Services</h3><p>Electrical troubleshooting and repair for all commercial kitchen equipment and power systems.</p></div>
    </div>
  </div>
</section>

<section class="equip">
  <div class="wrap">
    <div class="section-head">
      <h2>Equipment We Service</h2>
      <p>From ovens to fryers, we service all major brands and types of commercial kitchen equipment</p>
    </div>
    <div class="equip-grid">
      <div class="card equip-card"><div class="equip-top"><div class="icon-dot"><svg viewBox="0 0 24 24"><path d="M6 14a6 6 0 1 1 12 0v4H6z"/></svg></div><h3>Cooking Equipment</h3></div><p>Professional repair and maintenance for all types of commercial cooking ovens and ranges.</p><div class="tags"><span class="tag">Commercial Ovens</span><span class="tag">Convection Ovens</span><span class="tag">Combi Ovens</span><span class="tag">Steam Ovens</span><span class="tag">Deck Ovens</span></div></div>
      <div class="card equip-card"><div class="equip-top"><div class="icon-dot"><svg viewBox="0 0 24 24"><path d="M12 3c3 4 6 6 6 11a6 6 0 0 1-12 0c0-3 2-5 3-6 0 2 1 3 2 3 0-3 0-5 1-8z"/></svg></div><h3>Grills &amp; Griddles</h3></div><p>Expert service for all grilling equipment to ensure consistent cooking performance.</p><div class="tags"><span class="tag">Char Grills</span><span class="tag">Flat Top Griddles</span><span class="tag">Salamanders</span><span class="tag">Broilers</span><span class="tag">Panini Grills</span></div></div>
      <div class="card equip-card"><div class="equip-top"><div class="icon-dot"><svg viewBox="0 0 24 24"><path d="M6 3v8a2 2 0 0 0 4 0V3M8 11v10M16 3c-2 2-2 6 0 8v10"/></svg></div><h3>Fryers &amp; Steamers</h3></div><p>Specialized maintenance for frying and steaming equipment to maintain food quality.</p><div class="tags"><span class="tag">Deep Fryers</span><span class="tag">Pressure Fryers</span><span class="tag">Steam Tables</span><span class="tag">Food Steamers</span><span class="tag">Tilting Skillets</span></div></div>
      <div class="card equip-card"><div class="equip-top"><div class="icon-dot"><svg viewBox="0 0 24 24"><path d="M5 8h11v7a4 4 0 0 1-4 4H9a4 4 0 0 1-4-4zM16 10h2a2 2 0 0 1 0 4h-2"/></svg></div><h3>Beverage Equipment</h3></div><p>Professional service for all commercial beverage preparation equipment.</p><div class="tags"><span class="tag">Espresso Machines</span><span class="tag">Coffee Brewers</span><span class="tag">Tea Brewers</span><span class="tag">Hot Water Dispensers</span><span class="tag">Beverage Warmers</span></div></div>
      <div class="card equip-card"><div class="equip-top"><div class="icon-dot"><svg viewBox="0 0 24 24"><path d="M4 20L12 4l8 16zM9 14h6"/></svg></div><h3>Specialty Equipment</h3></div><p>Expert repair services for specialized cooking and food preparation equipment.</p><div class="tags"><span class="tag">Pizza Ovens</span><span class="tag">Rotisseries</span><span class="tag">Warming Cabinets</span><span class="tag">Heat Lamps</span><span class="tag">Food Processors</span></div></div>
      <div class="card equip-card"><div class="equip-top"><div class="icon-dot"><svg viewBox="0 0 24 24"><path d="M4 11h16a8 8 0 0 1-16 0zM8 7c0-2 2-2 2-4M13 7c0-2 2-2 2-4"/></svg></div><h3>Food Prep Equipment</h3></div><p>Comprehensive maintenance for all food preparation and cleaning equipment.</p><div class="tags"><span class="tag">Mixers</span><span class="tag">Slicers</span><span class="tag">Dishwashers</span><span class="tag">Prep Tables</span><span class="tag">Food Warmers</span></div></div>
    </div>
  </div>
</section>

<section class="why">
  <div class="wrap">
    <div class="section-head">
      <h2>Why Choose Junction Kitchen Service?</h2>
      <p>We're the trusted partner for restaurant owners who demand reliability, expertise, and exceptional service</p>
    </div>
    <div class="stats">
      <div><div class="stat-value">500+</div><div class="stat-label">Restaurants Served</div></div>
      <div><div class="stat-value">24/7</div><div class="stat-label">Emergency Response</div></div>
      <div><div class="stat-value">98%</div><div class="stat-label">Customer Satisfaction</div></div>
      <div><div class="stat-value">2hr</div><div class="stat-label">Average Response Time</div></div>
    </div>
    <div class="why-grid">
      <div class="card why-card"><div class="icon-dot"><svg viewBox="0 0 24 24"><circle cx="12" cy="9" r="5"/><path d="M9 13l-1 8 4-2 4 2-1-8"/></svg></div><span class="pill">Industry Leader</span><h3>25+ Years Experience</h3><p>Over two decades of expertise in commercial kitchen equipment service and repair.</p></div>
      <div class="card why-card"><div class="icon-dot"><svg viewBox="0 0 24 24"><circle cx="12" cy="12" r="9"/><path d="M12 7v5l3 2"/></svg></div><span class="pill">Always Available</span><h3>24/7 Emergency Service</h3><p>Round-the-clock emergency repairs to minimize downtime and lost revenue.</p></div>
      <div class="card why-card"><div class="icon-dot"><svg viewBox="0 0 24 24"><circle cx="9" cy="8" r="3"/><path d="M3 20a6 6 0 0 1 12 0M16 5a3 3 0 0 1 0 6M21 20a6 6 0 0 0-4-6"/></svg></div><span class="pill">Expert Team</span><h3>Certified Technicians</h3><p>Factory-trained and certified technicians for all major equipment brands.</p></div>
      <div class="card why-card tall"><div class="icon-dot"><svg viewBox="0 0 24 24"><path d="M14 6a4 4 0 0 0 5 5l-9 9a2 2 0 0 1-3-3l9-9"/></svg></div><span class="pill">Brand Authorized</span><h3>All Major Brands</h3><p>Authorized service for Ardent, Kestrel, Halden, Northvale, and many more.</p></div>
      <div class="card why-card tall"><div class="icon-dot"><svg viewBox="0 0 24 24"><path d="M12 3l8 3v6c0 5-4 8-8 9-4-1-8-4-8-9V6z"/></svg></div><span class="pill">Guaranteed Work</span><h3>Warranty Protection</h3><p>All repairs backed by comprehensive warranties and satisfaction guarantees.</p></div>
      <div class="card why-card tall"><div class="icon-dot"><svg viewBox="0 0 24 24"><path d="M12 3l2.7 5.6 6.1.8-4.5 4.2 1.1 6.1L12 16.8 6.6 19.7l1.1-6.1L3.2 9.4l6.1-.8z"/></svg></div><span class="pill">Proactive Care</span><h3>Preventive Programs</h3><p>Customized maintenance programs to prevent breakdowns and extend equipment life.</p></div>
    </div>
  </div>
</section>

<section class="trusted">
  <div class="wrap">
    <div class="trusted-copy">
      <h2>Trusted by Commercial<br>Kitchens Nationwide</h2>
      <p>For over two decades, Junction Kitchen Service has been the go-to partner for restaurants, hotels, and commercial kitchens seeking reliable equipment service and repair. Our team of certified technicians brings unmatched expertise to every job.</p>
      <div class="checks">
        <div class="check"><svg viewBox="0 0 24 24"><circle cx="12" cy="12" r="9"/><path d="M8 12l3 3 5-6"/></svg>Certified technicians with 15+ years experience</div>
        <div class="check"><svg viewBox="0 0 24 24"><circle cx="12" cy="12" r="9"/><path d="M8 12l3 3 5-6"/></svg>Same-day service available in most areas</div>
        <div class="check"><svg viewBox="0 0 24 24"><circle cx="12" cy="12" r="9"/><path d="M8 12l3 3 5-6"/></svg>Comprehensive warranty on all repairs</div>
        <div class="check"><svg viewBox="0 0 24 24"><circle cx="12" cy="12" r="9"/><path d="M8 12l3 3 5-6"/></svg>Specialized in commercial cooking equipment</div>
        <div class="check"><svg viewBox="0 0 24 24"><circle cx="12" cy="12" r="9"/><path d="M8 12l3 3 5-6"/></svg>Emergency 24/7 support hotline</div>
        <div class="check"><svg viewBox="0 0 24 24"><circle cx="12" cy="12" r="9"/><path d="M8 12l3 3 5-6"/></svg>Preventive maintenance programs</div>
      </div>
    </div>
    <div class="trusted-visual">
      <div class="trusted-frame"><div class="trusted-photo" role="img" aria-label="Technician in blue cap and apron servicing a commercial oven"></div></div>
      <div class="badge-light"><strong>1000+</strong><span>Satisfied Clients</span></div>
      <div class="badge-teal"><strong>20+</strong><span>Years of Experience</span></div>
    </div>
  </div>
</section>

<section class="reviews">
  <div class="wrap">
    <div class="section-head">
      <h2>What Our Clients Say</h2>
      <p>Don't just take our word for it - hear from the restaurant owners and kitchen managers who trust us</p>
    </div>
    <div class="review-grid">
      <div class="card review"><div class="stars">★★★★★</div><h3>Elena Marquez</h3><div class="role">Head Chef, Casa Olivo Restaurant</div><blockquote>"Junction saved our busy Friday night when our main grill went down. Their technician arrived within an hour and had us back up and running. Exceptional service!"</blockquote></div>
      <div class="card review"><div class="stars">★★★★★</div><h3>Daniel Park</h3><div class="role">Kitchen Manager, Harbor Hotel</div><blockquote>"We've been using Junction for our preventive maintenance for 3 years. Their proactive approach has prevented major breakdowns and saved us thousands."</blockquote></div>
      <div class="card review"><div class="stars">★★★★★</div><h3>Rachel Moore</h3><div class="role">Owner, Moore's Bistro</div><blockquote>"Professional, reliable, and knowledgeable. The team at Junction understands the urgency of kitchen equipment issues and always delivers quality work."</blockquote></div>
    </div>
  </div>
</section>

<section class="contact">
  <div class="wrap">
    <div class="section-head">
      <h2>Get Professional Service Today</h2>
      <p>Ready to get your equipment serviced? Contact us for a quick response and expert solutions.</p>
    </div>
    <div class="contact-grid">
      <div class="card contact-card"><div class="icon-dot"><svg viewBox="0 0 24 24"><path d="M5 3h4l2 5-3 2a11 11 0 0 0 6 6l2-3 5 2v4a2 2 0 0 1-2 2A17 17 0 0 1 3 5a2 2 0 0 1 2-2z"/></svg></div><h3>24/7 Emergency</h3><div class="val big">(555) 014-2368</div><div class="note">Always available</div></div>
      <div class="card contact-card"><div class="icon-dot"><svg viewBox="0 0 24 24"><rect x="3" y="5" width="18" height="14" rx="2"/><path d="M3 7l9 6 9-6"/></svg></div><h3>Email Support</h3><div class="val">service@junctionkitchen.com</div><div class="note">2-hour response</div></div>
      <div class="card contact-card"><div class="icon-dot"><svg viewBox="0 0 24 24"><path d="M12 21s7-6 7-11a7 7 0 0 0-14 0c0 5 7 11 7 11z"/><circle cx="12" cy="10" r="2.5"/></svg></div><h3>Service Area</h3><div class="val">Nationwide Coverage</div><div class="note">Local technicians</div></div>
      <div class="card contact-card"><div class="icon-dot"><svg viewBox="0 0 24 24"><circle cx="12" cy="12" r="9"/><path d="M12 7v5l3 2"/></svg></div><h3>Business Hours</h3><div class="val">Mon-Fri: 7AM-7PM</div><div class="note">Weekend service available</div></div>
    </div>
    <div class="card form-card">
      <div class="form-title"><svg viewBox="0 0 24 24"><circle cx="12" cy="12" r="9"/><path d="M8 12l3 3 5-6"/></svg><h3>Request Professional Service</h3></div>
      <p class="form-sub">Fill out this form and we'll get back to you within 2 hours during business hours.</p>
      <div class="form-cols">
        <div>
          <h4>Contact Information</h4>
          <div class="field"><label>Full Name *</label><div class="input"></div></div>
          <div class="field"><label>Email Address *</label><div class="input"></div></div>
          <div class="field"><label>Phone Number *</label><div class="input"></div></div>
          <div class="field"><label>Restaurant/Company Name</label><div class="input"></div></div>
        </div>
        <div>
          <h4>Service Details</h4>
          <div class="field"><label>Service Type *</label><div class="input select">Select service type ⌄</div></div>
          <div class="field"><label>Urgency Level *</label><div class="input select">Select urgency ⌄</div></div>
          <div class="field"><label>Equipment Details &amp; Issue Description *</label><div class="input area">Please describe the equipment type, model (if known), and the issue you're experiencing...</div></div>
        </div>
      </div>
      <span class="btn submit">Submit Service Request <svg width="16" height="16" viewBox="0 0 16 16" fill="none" stroke="#fff" stroke-width="2"><path d="M3 8h10M9 4l4 4-4 4"/></svg></span>
      <p class="form-note">We'll contact you within 2 hours during business hours</p>
    </div>
  </div>
</section>

<footer class="footer">
  <div class="wrap">
    <div class="footer-top">
      <div class="footer-about">
        <div class="brand"><span class="brand-mark"></span><span class="brand-name">Junction</span></div>
        <p>Professional commercial cooking equipment service and repair. Trusted by restaurants and commercial kitchens nationwide for over 20 years.</p>
        <div class="line"><b>Emergency Service:</b> (555) 014-2368</div>
        <div class="line"><b>Email:</b> service@junctionkitchen.com</div>
      </div>
      <div class="footer-col"><h4>Services</h4><ul><li>Equipment Repair</li><li>Preventive Maintenance</li><li>Emergency Service</li><li>Staff Training</li><li>Safety Inspections</li><li>Installation Services</li></ul></div>
      <div class="footer-col"><h4>Equipment We Service</h4><ul><li>Commercial Ovens</li><li>Grills &amp; Griddles</li><li>Fryers</li><li>Ranges &amp; Cooktops</li><li>Steamers</li><li>Warming Equipment</li></ul></div>
    </div>
    <div class="footer-bottom"><span>© 2025 Junction Kitchen Service. All rights reserved.</span><nav><span>Privacy Policy</span><span>Terms of Service</span><span>Service Areas</span></nav></div>
  </div>
</footer>

</div>
</body>
</html>
```